I need jar labels, and other types to include round and cigar band with an already designed logo

Need a round sticker to place on products, jar labels, 3 sizes with 1 label having 3 different names. also reflect my design on a thank you card and round sticker
I would like a 10 " cigar band with my logo in the middle for handmade bars of soap

Target Market(s)

This project will be for labeling my products for my e-commerce business

Industry/Entity Type

Beauty

Font styles to use
Serif

Colors
e667a6
ffcf3e

Requirements
Must have
• The labels must contain my logo. I need (4) 1.5" X 4" label with my logo and the words: Handmade Sugar Scrub, Handmade Whipped Body Butter, Handmade Whipped Soap Scrub, Handmade Salt Scrub

I also must have a round sticker 2' in diameter with my logo in Gold

I also need a round sticker I rose gold that reflects my logo and says thank you for supporting my small business.
Nice to have
• I want round and rectangle labels for products that contain my logo. I also need thank you cards and thank you for your order sticker with my logo
Should not have
• do not change the color of my logo and make the print on the labels in Black

```html
<!DOCTYPE html>
<html lang="en">
<head>
<meta charset="utf-8">
<title>Soak and Lather – Label Set</title>
<link rel="stylesheet" href="https://fonts.googleapis.com/css2?family=Montserrat:wght@400;700&family=Great+Vibes&family=Alex+Brush&display=swap">
<style>
  :root {
    --page: #ffffff;
    --gold: #d9b53c;
    --gold-light: #f3dc6a;
    --salt: #8000ff;
    --soap-scrub: #007d27;
    --body-butter: #47321b;
    --sugar: #c30016;
    --soap-band: #0033f0;
    --thanks: #b1008f;
    --thanks-pink: #f0a8c8;
    --rule: #a9a9a9;
    --rule-text: #8c8c8c;
  }
  * { margin: 0; padding: 0; box-sizing: border-box; }
  html, body { width: 939px; height: 1200px; overflow: hidden; background: var(--page); }
  .sheet { position: relative; width: 939px; height: 1200px; font-family: "Montserrat", sans-serif; }

  .dimensions { position: absolute; inset: 0; width: 939px; height: 1200px; }
  .dimensions line { stroke: var(--rule); stroke-width: 0.7; }
  .dimensions text { fill: var(--rule-text); font-family: "Montserrat", sans-serif; font-size: 11px; text-anchor: middle; }

  .jar-label { position: absolute; left: 82px; width: 442px; height: 163px; text-align: center; color: var(--gold); }
  .jar-label--salt { top: 44px; background: var(--salt); }
  .jar-label--soap-scrub { top: 232px; height: 152px; background: var(--soap-scrub); }
  .jar-label--body-butter { top: 414px; height: 153px; background: var(--body-butter); }
  .jar-label--sugar { top: 597px; height: 152px; background: var(--sugar); }

  .brand-name { font-weight: 400; color: var(--gold-light); letter-spacing: 0.02em; white-space: nowrap; }
  .jar-label .brand-name { position: absolute; top: 40px; left: 0; right: 0; font-size: 9.5px; }

  .handmade { font-family: "Great Vibes", cursive; line-height: 1; }
  .jar-label .handmade { position: absolute; top: 72px; left: 0; right: 0; font-size: 24px; }
  .jar-label--salt .handmade { color: #b070f0; }
  .jar-label--soap-scrub .handmade { color: #3cc04a; }
  .jar-label--body-butter .handmade { color: #7a6040; }
  .jar-label--sugar .handmade { color: #ff5a6a; }

  .product-name { font-weight: 700; letter-spacing: 0.04em; line-height: 1.15; font-size: 17.5px; color: var(--gold); }
  .jar-label .product-name { position: absolute; top: 99px; left: 0; right: 0; }

  .soap-band { position: absolute; left: 587px; top: 44px; width: 255px; height: 1092px; background: var(--soap-band); text-align: center; }
  .soap-band .brand-name { position: absolute; top: 530px; left: 0; right: 0; font-size: 16px; }
  .soap-band .handmade { position: absolute; top: 582px; left: 0; right: 0; font-size: 46px; color: #4a8cff; }
  .soap-band .product-name { position: absolute; top: 636px; left: 0; right: 0; font-size: 34px; }

  .round-sticker { position: absolute; width: 221px; height: 221px; border-radius: 50%; text-align: center; }
  .round-sticker--thanks { left: 73px; top: 866px; background: var(--thanks); }
  .round-sticker--thanks .brand-name { position: absolute; top: 62px; left: 0; right: 0; font-size: 11px; color: var(--thanks-pink); }
  .thank-you-note { position: absolute; top: 108px; left: 0; right: 0; font-family: "Alex Brush", cursive; font-size: 20px; line-height: 1.2; color: #ffffff; }

  .round-sticker--gold { left: 330px; top: 866px; border: 3px solid var(--gold); }
  .round-sticker--gold .seal { position: absolute; left: 34px; top: 34px; width: 147px; height: 147px; border-radius: 50%; background: radial-gradient(circle at 50% 35%, var(--gold-light), #a88414); }
  .round-sticker--gold .brand-name { position: absolute; top: 100px; left: 0; right: 0; font-size: 13px; font-weight: 700; color: var(--gold); }
</style>
</head>
<body>
<main class="sheet">
  <svg class="dimensions" viewBox="0 0 939 1200" aria-hidden="true">
    <line x1="82" y1="33" x2="287" y2="33"/><line x1="323" y1="33" x2="524" y2="33"/>
    <line x1="82" y1="24" x2="82" y2="44"/><line x1="524" y1="24" x2="524" y2="44"/>
    <text x="305" y="37">4”</text>
    <line x1="541" y1="46" x2="541" y2="108"/><line x1="541" y1="146" x2="541" y2="208"/>
    <line x1="528" y1="46" x2="550" y2="46"/><line x1="528" y1="208" x2="550" y2="208"/>
    <text x="543" y="131">1.5”</text>
    <line x1="587" y1="33" x2="688" y2="33"/><line x1="733" y1="33" x2="842" y2="33"/>
    <line x1="587" y1="24" x2="587" y2="44"/><line x1="842" y1="24" x2="842" y2="44"/>
    <text x="714" y="37">2,3”</text>
    <line x1="858" y1="46" x2="858" y2="566"/><line x1="858" y1="616" x2="858" y2="1137"/>
    <line x1="842" y1="46" x2="865" y2="46"/><line x1="842" y1="1137" x2="865" y2="1137"/>
    <text x="857" y="596">10”</text>
    <line x1="73" y1="1102" x2="163" y2="1102"/><line x1="205" y1="1102" x2="294" y2="1102"/>
    <line x1="73" y1="976" x2="73" y2="1108"/><line x1="294" y1="976" x2="294" y2="1108"/>
    <text x="184" y="1106">2”</text>
    <line x1="330" y1="1102" x2="419" y2="1102"/><line x1="462" y1="1102" x2="551" y2="1102"/>
    <line x1="330" y1="976" x2="330" y2="1108"/><line x1="551" y1="976" x2="551" y2="1108"/>
    <text x="440" y="1106">2”</text>
  </svg>

  <section class="jar-label jar-label--salt">
    <p class="brand-name">SOAK AND LATHER</p>
    <p class="handmade">handmade</p>
    <h2 class="product-name">SALT<br>SCRUB</h2>
  </section>

  <section class="jar-label jar-label--soap-scrub">
    <p class="brand-name">SOAK AND LATHER</p>
    <p class="handmade">handmade</p>
    <h2 class="product-name">WHIPPED SOAP<br>SCRUB</h2>
  </section>

  <section class="jar-label jar-label--body-butter">
    <p class="brand-name">SOAK AND LATHER</p>
    <p class="handmade">handmade</p>
    <h2 class="product-name">WHIPPED BODY<br>BUTTER</h2>
  </section>

  <section class="jar-label jar-label--sugar">
    <p class="brand-name">SOAK AND LATHER</p>
    <p class="handmade">handmade</p>
    <h2 class="product-name">SUGAR<br>SCRUB</h2>
  </section>

  <section class="soap-band">
    <p class="brand-name">SOAK AND LATHER</p>
    <p class="handmade">handmade</p>
    <h2 class="product-name">SOAP</h2>
  </section>

  <section class="round-sticker round-sticker--thanks">
    <p class="brand-name">SOAK AND LATHER</p>
    <p class="thank-you-note">Thank you<br>for supporting my<br>small business!</p>
  </section>

  <section class="round-sticker round-sticker--gold">
    <div class="seal" role="img" aria-label="Gold seal area"></div>
    <p class="brand-name">SOAK AND LATHER</p>
  </section>
</main>
</body>
</html>
```